Pregnancy and Fertility Information Website

Hello Designers,
I need a website which provide tips and information about healthy and happy pregnancy. My website name is Lorvin medical.

The website should provide all the information needed throughout pregnancy and beyond ranging from pregnancy tracking tools and articles about common pregnancy concerns and what to expect during pregnancy,etc.
The details about first trimester, second trimester and third trimester should be highlighted in the website.

Top Navigation
Home, Fertility, Pregnancy basics, Articles, Tips and News

I'm looking for a simple and clean design which involves captivating images and colors but it shouldn't be crowded. The design must be professional and modern. An easy to navigate layout is a must.

Green, violet, blue and light yellow colors are my favorites but i'm open to other options.

Any questions. Kindly ask

Industry/Entity Type

Medical

```html
<!DOCTYPE html>
<html lang="en">
<head>
<meta charset="utf-8">
<title>Lorvin medical</title>
<link href="https://fonts.googleapis.com/css2?family=Open+Sans:wght@400;600;700&display=swap" rel="stylesheet">
<style>
:root{
  --page:#f2f2f2;
  --white:#ffffff;
  --navy:#173a8a;
  --navy-light:#2c63b3;
  --hero-green:#c6e6a7;
  --hero-text:#2a6a2c;
  --teal-line:#4a93b5;
  --yellow-a:#e4e23a;
  --yellow-b:#f7f8a0;
  --dot:#3f8fc8;
  --ink:#1e1e1e;
  --brand-green:#6fb24a;
  --brand-blue:#2a6bb0;
}
*{margin:0;padding:0;box-sizing:border-box}
html,body{width:1092px;height:1200px;overflow:hidden;background:var(--page)}
body{font-family:"Open Sans",Arial,sans-serif;color:var(--ink);position:relative}
.site-header{position:absolute;left:0;top:0;width:1092px;height:146px;background:var(--page)}
.brand{position:absolute;left:72px;top:50px;display:flex;align-items:center;gap:12px}
.brand-dot{width:44px;height:44px;border-radius:50%;background:var(--brand-blue)}
.brand-name{font-size:26px;font-weight:600;color:var(--brand-blue)}
.social{position:absolute;left:885px;top:96px;display:flex;gap:8px}
.social span{width:39px;height:39px;border-radius:4px;background:var(--navy-light)}
.main-nav{position:absolute;left:0;top:146px;width:1092px;height:49px;background:linear-gradient(90deg,var(--navy),var(--navy-light))}
.main-nav a{position:absolute;top:11px;color:var(--white);font-size:21px;text-decoration:none}
.hero{position:absolute;left:0;top:195px;width:1092px;height:278px;background:var(--hero-green)}
.hero-photo{position:absolute;left:0;top:0;width:477px;height:278px;background:linear-gradient(90deg,#e9dcd3,#b9857a 55%,#cfa79a)}
.hero-title{position:absolute;left:520px;top:62px;width:520px;font-size:33px;line-height:46px;color:var(--hero-text)}
.hero-rule{position:absolute;left:0;top:473px;width:1092px;height:5px;background:var(--teal-line)}
.slider-band{position:absolute;left:0;top:478px;width:1092px;height:47px;background:linear-gradient(90deg,var(--yellow-a),var(--yellow-b) 45%,var(--yellow-b) 60%,var(--yellow-a))}
.slider-dots{position:absolute;left:477px;top:493px;display:flex;gap:14px}
.slider-dots span{width:15px;height:15px;border-radius:50%;border:2px solid var(--dot)}
.slider-dots span.active{background:var(--dot)}
.feature-strip{position:absolute;left:0;top:525px;width:1092px;height:170px;background:var(--white)}
.feature-tile{position:absolute;top:9px;height:146px}
.topics{position:absolute;left:0;top:695px;width:1092px;height:291px;background:var(--page)}
.topic-text{position:absolute;top:36px;font-size:18px;line-height:24.5px}
.topic-left{left:52px;width:470px}
.topic-right{left:594px;width:430px}
.topic-divider{position:absolute;left:546px;top:12px;width:2px;height:268px;background:var(--navy)}
.site-footer{position:absolute;left:0;top:986px;width:1092px;height:214px;background:linear-gradient(90deg,var(--navy),var(--navy-light) 55%,var(--navy))}
.footer-brand{position:absolute;left:472px;top:80px;display:flex;align-items:center;gap:10px}
.footer-brand .brand-dot{width:34px;height:34px;background:var(--brand-green)}
.footer-brand .brand-name{color:var(--white);font-size:22px}
.contact{position:absolute;color:var(--white);font-size:16px;line-height:22px}
.contact strong{display:block;font-weight:700;font-size:17px;margin-bottom:3px}
.contact svg{position:absolute;left:-46px;top:0}
.office{left:118px;top:100px}
.call{left:840px;top:100px}
</style>
</head>
<body>
<header class="site-header">
  <div class="brand"><span class="brand-dot"></span><span class="brand-name">Lorvin medical</span></div>
  <div class="social" aria-label="Social links"><span></span><span></span><span></span><span></span></div>
</header>
<nav class="main-nav">
  <a href="#" style="left:100px">HOME</a>
  <a href="#" style="left:220px">Fertility</a>
  <a href="#" style="left:343px">Pregnancy basics</a>
  <a href="#" style="left:559px">Articles</a>
  <a href="#" style="left:693px">Tips</a>
  <a href="#" style="left:795px">News</a>
</nav>
<section class="hero">
  <div class="hero-photo" role="img" aria-label="Pregnant woman in a pink top holding her belly"></div>
  <h1 class="hero-title" style="font-weight:400">how should women facing labor approach their birth plan?</h1>
</section>
<div class="hero-rule"></div>
<div class="slider-band"></div>
<div class="slider-dots"><span class="active"></span><span></span><span></span></div>
<section class="feature-strip">
  <div class="feature-tile" style="left:42px;width:240px;background:linear-gradient(135deg,#c84a2a,#8aa83a 50%,#d9b070)" role="img" aria-label="Basket of fresh vegetables and bread"></div>
  <div class="feature-tile" style="left:313px;width:214px;background:linear-gradient(135deg,#f4f4f4,#d9e2de 50%,#e8e0d4)" role="img" aria-label="Capsules over a molecular diagram"></div>
  <div class="feature-tile" style="left:560px;width:222px;background:linear-gradient(135deg,#e6e2df,#c9b7c9 55%,#8d7aa6)" role="img" aria-label="Doctor talking with a pregnant patient"></div>
  <div class="feature-tile" style="left:820px;width:220px;background:linear-gradient(135deg,#bcdcea,#cfe6ef 60%,#e8c9b8)" role="img" aria-label="Hand holding a pregnancy test"></div>
</section>
<section class="topics">
  <p class="topic-text topic-left">In contrast to women, there is no maximum age at which a man is unable to father a child. However, a man's sperm count and motility of sperm both decrease with age. Men over age 45 have been shown to take longer to achieve a pregnancy when trying to conceive. You may wish to discuss with your doctor ways to enhance your chances for conception if your partner is older.</p>
  <div class="topic-divider"></div>
  <p class="topic-text topic-right">Some lifestyle modifications may be able to boost male fertility, like maintaining a healthy weight, managing stress, and avoiding tobacco and alcohol use. Eating a diet high in zinc (meats, whole grains, eggs, and seafood), vitamin E, and selenium (meats, seafood, mushrooms, Brazil nuts, and cereals) may also help. Keeping the testicles cool can improve male fertility; hot tubs, hot baths, and saunas can all reduce sperm count.</p>
</section>
<footer class="site-footer">
  <div class="contact office">
    <svg width="26" height="34" viewBox="0 0 26 34" aria-hidden="true"><path d="M13 2a10 10 0 0 0-10 10c0 8 10 19 10 19s10-11 10-19A10 10 0 0 0 13 2z" fill="none" stroke="#fff" stroke-width="2.5"/><circle cx="13" cy="12" r="3.5" fill="#fff"/></svg>
    <strong>HeadOffice</strong>48 Alder Row, Ste 310,<br>Brookfield, CA. 94522
  </div>
  <div class="footer-brand"><span class="brand-dot"></span><span class="brand-name">Lorvin medical</span></div>
  <div class="contact call">
    <svg width="38" height="38" viewBox="0 0 38 38" aria-hidden="true"><circle cx="19" cy="19" r="17" fill="none" stroke="#fff" stroke-width="2.5"/><path d="M13 10l4 0 2 5-2.5 2a11 11 0 0 0 5 5l2-2.5 5 2 0 4c-9 1-17-7-16-16z" fill="#fff"/></svg>
    <strong>Call Us</strong>001 555 014 2267
  </div>
</footer>
</body>
</html>
```